Tolvik's Trim spring flyers

I am needing a flyer design for my lawn mowing business. my services are mowing, edging, weed eating, vacuuming with strong attention to detail. residential and commercial. Mowing average $35 and Spring clean up average $79. Looking for fun, professional and colorful to grab the eye and stand out. rough sizing of 10"x4"

Target Market(s)

people needing lawn care and spring clean up

Font styles to use
Serif

Colors

Designer to choose colors to be used in the design.

Requirements
Must have
• Services listed and pricing listed
• please add licensed and insured
• 417-555-0183
• dorsebrian7@fernmail.test
• FREE ESTIMATES

```html
<!DOCTYPE html>
<html lang="en">
<head>
<meta charset="utf-8">
<title>Tolvik's Trim Lawn Care – Spring Flyer</title>
<link rel="stylesheet" href="https://fonts.googleapis.com/css2?family=Fredoka:wght@700&family=Roboto+Slab:wght@800;900&display=swap">
<style>
  :root {
    --page: #ecebe8;
    --white: #f7f6f8;
    --brand-blue: #1d72b8;
    --edge-blue: #2f86d0;
    --edge-light: #a9d2f0;
    --charcoal: #3b3b3d;
    --offer-pink: #c2127a;
    --headline-yellow: #ffe81a;
    --headline-pink: #d4137f;
    --lawn-dark: #2f6a1f;
    --lawn-mid: #4f9a2c;
    --lawn-light: #7cbd45;
    --foliage: #3f6e2c;
    --text-white: #ffffff;
  }
  * { box-sizing: border-box; margin: 0; padding: 0; }
  html, body { width: 1200px; height: 800px; overflow: hidden; }
  body { background: var(--page); position: relative; }

  .flyer {
    position: absolute; left: 40px; top: 176px;
    width: 1120px; height: 448px; overflow: hidden;
    background: var(--lawn-mid);
    box-shadow: 0 6px 18px rgba(0,0,0,.25);
  }
  .lawn-photo {
    position: absolute; inset: 0;
    background: linear-gradient(180deg, var(--foliage) 0%, #5c8f3a 22%, var(--lawn-light) 32%, var(--lawn-mid) 55%, var(--lawn-dark) 100%);
  }
  .shapes { position: absolute; inset: 0; }

  .brand {
    position: absolute; left: 12px; top: 88px; width: 265px;
    display: flex; align-items: center; justify-content: center; gap: 10px;
  }
  .brand-square { flex: 0 0 22px; width: 22px; height: 22px; background: var(--brand-blue); }
  .brand-name {
    font-family: "Roboto Slab", serif; font-weight: 800;
    font-size: 27px; line-height: 1; color: var(--brand-blue); white-space: nowrap;
  }

  .offer-tab {
    position: absolute; left: 0; top: 202px; width: 34px; height: 124px;
    background: var(--offer-pink); border-radius: 0 4px 4px 0;
    display: flex; align-items: center; justify-content: center;
  }
  .offer-tab span {
    transform: rotate(-90deg); white-space: nowrap;
    font-family: "Roboto Slab", serif; font-weight: 900; font-size: 15px;
    color: var(--headline-yellow); letter-spacing: .5px;
  }

  .headline {
    position: absolute; left: 46px; top: 188px;
    transform: rotate(-4deg); transform-origin: left top;
    font-family: "Fredoka", sans-serif; font-weight: 700;
    color: var(--headline-yellow); line-height: 66px; white-space: nowrap;
    text-shadow:
      -1px -1px 0 #fff, 1px -1px 0 #fff,
      2px 2px 0 var(--headline-pink), 3px 3px 0 var(--headline-pink),
      4px 4px 0 var(--headline-pink), 5px 5px 0 var(--headline-yellow),
      6px 6px 0 var(--headline-pink);
  }
  .headline .price-line { display: block; font-size: 68px; }

  .services {
    position: absolute; left: 36px; top: 342px;
    font-family: "Roboto Slab", serif; font-weight: 800;
    font-size: 19px; line-height: 22px; color: var(--text-white);
    text-shadow: 1px 2px 2px rgba(0,0,0,.55);
  }

  .contact {
    position: absolute; right: 75px; top: 354px; text-align: right;
    font-family: "Roboto Slab", serif; font-weight: 800; color: var(--text-white);
  }
  .contact-label { font-size: 11px; }
  .contact-phone { font-size: 23px; font-weight: 900; letter-spacing: 1px; margin: 1px 0 4px; }
  .contact-credentials { font-size: 11px; margin-bottom: 6px; }
  .contact-email { font-size: 11px; }
</style>
</head>
<body>
  <article class="flyer">
    <div class="lawn-photo" role="img" aria-label="Photo of a freshly striped green lawn in front of a house with shrubs and trees, a worker in a blue shirt trimming grass on the right"></div>

    <svg class="shapes" viewBox="0 0 1120 448" width="1120" height="448" aria-hidden="true">
      <path d="M0 0 H553 C430 60 300 170 150 185 C80 190 30 170 0 160 Z" fill="var(--white)"/>
      <path d="M553 0 C430 60 300 170 150 185 C80 190 30 170 0 160" fill="none" stroke="var(--edge-blue)" stroke-width="4"/>
      <path d="M503 448 C650 380 800 320 960 318 C1040 318 1090 340 1120 356 V448 Z" fill="var(--charcoal)"/>
      <path d="M495 448 C650 378 800 318 960 316 C1040 316 1090 338 1120 354" fill="none" stroke="var(--edge-light)" stroke-width="6"/>
      <path d="M560 420 C680 365 810 318 960 316 C1040 316 1090 338 1120 354" fill="none" stroke="var(--edge-blue)" stroke-width="3"/>
    </svg>

    <div class="brand">
      <span class="brand-square"></span>
      <span class="brand-name">TOLVIK'S TRIM</span>
    </div>

    <div class="offer-tab"><span>OUR OFFER</span></div>

    <h1 class="headline">
      <span class="price-line">MOWING AVERAGE $35</span>
      <span class="price-line">SPRING CLEANUP AVERAGE $79</span>
    </h1>

    <p class="services">
      MY SERVICES:<br>
      MOWING, EDGING, WEED EATING, VACUUMING WITH<br>
      STRONG ATTENTION TO DETAIL.<br>
      RESIDENTIAL AND COMMERCIAL.
    </p>

    <div class="contact">
      <p class="contact-label">FREE ESTIMATES – CALL:</p>
      <p class="contact-phone">417-555-0183</p>
      <p class="contact-credentials">LICENSED AND INSURED · LAWN CARE</p>
      <p class="contact-email">DORSEBRIAN7@FERNMAIL.TEST</p>
    </div>
  </article>
</body>
</html>
```